Business Card Design: Pregnancy and Parenting Education/Support

My company is called Harborlux and the tagline is Guiding Every Step Together. I'm based in Greater Boston and work with families from pregnancy up until 6 months old, supporting them with baby gift registry and gear consultations, postpartum doula services (in-home newborn and family care), new mom support groups for first-time and second-time moms, and various parenting and gear workshops. I also have an informational blog.

I am selling myself as my business: it's just me! I am looking for designs that convey my professional expertise in the field (I have broad experience) as well as my warm, passionate, caring, empathic, and nurturing demeanor. I want to invoke feelings of trust, serenity, collaboration, and stability, and I want to be able to reach parents of any gender and family type, as well as businesses. I want to be that blend of professional and trusted friend.

I'd like to see green (I like the green on my website! www.harborluxparenting.com) to go along with the seedling image.

The pic I attached is horrible, but I really like the image of Harborlux in a simple, easily readable and transferrable logo.
Updates

Incorporation of a simple, readable logo that inspires nurturing, community, trust, and kindness; and imagery not only of seedlings but of tending/nurturing seedlings, would be awesome!

Target Market(s)

Expectant/new families: men and women ages 20-40, middle class. Also, other business owners, large and small, in pregnancy and parenting-related field

Industry/Entity Type

Baby

Contact Information for Business Card

Harborlux, Guiding Every Step Together, Marisol Penwarden, Owner/Founder, www.harborluxparenting.com, mpenwarden@harborluxparenting.com, 617-555-0193, Serving Greater Boston (If there's space/it makes sense: @HarborluxbyMP, Kinbook.com/HarborluxParenting)

Requirements
Nice to have
• I like circles, and I like the imagery of nurturing seedlings that comes from my business name and tagline (Harborlux: Guiding Every Step Together). The horrible graphic attached is sort of an idea I have, but it might be too literal or too complicated to turn into a good, easily readable, easily transferrable logo? (Woman with arms around seedlings of different sizes, maybe roots going down?)

Also nice to have is twitter handle and Facebook name, but if it looks crowded, no worries! @HarborluxbyMP, facebook.com/HarborluxParenting

```html
<!DOCTYPE html>
<html lang="en">
<head>
<meta charset="utf-8">
<title>Harborlux Business Card</title>
<link rel="stylesheet" href="https://fonts.googleapis.com/css2?family=Arimo:wght@400;700&family=Delius&display=swap">
<style>
  :root {
    --page-bg: #dcd8d3;
    --brand-orange: #f15f22;
    --card-light-top: #f1f0f0;
    --card-light-bottom: #c9cbd3;
    --ink: #111111;
    --white: #ffffff;
  }
  html, body {
    margin: 0;
    width: 1200px;
    height: 900px;
    overflow: hidden;
    background: var(--page-bg);
  }
  .business-card {
    position: absolute;
    left: 100px;
    top: 164px;
    width: 1000px;
    height: 572px;
    background: linear-gradient(180deg, var(--card-light-top) 0%, #e3e3e6 50%, var(--card-light-bottom) 100%);
    box-shadow: 0 10px 30px rgba(0,0,0,0.25);
    font-family: "Arimo", Arial, sans-serif;
    overflow: hidden;
  }
  .owner-block {
    position: absolute;
    left: 70px;
    top: 26px;
    color: var(--ink);
  }
  .owner-name {
    margin: 0;
    font-size: 33px;
    font-weight: 700;
    text-transform: uppercase;
    letter-spacing: 0.5px;
  }
  .owner-title {
    margin: 2px 0 0 200px;
    font-size: 21px;
    font-weight: 700;
  }
  .phone {
    position: absolute;
    right: 36px;
    top: 74px;
    display: flex;
    align-items: center;
    gap: 14px;
    font-size: 33px;
    font-weight: 700;
    color: var(--ink);
  }
  .brand-band {
    position: absolute;
    left: 0;
    top: 120px;
    width: 100%;
    height: 276px;
    background: var(--brand-orange);
  }
  .band-rule {
    position: absolute;
    left: 0;
    width: 100%;
    height: 4px;
    background: var(--white);
    opacity: 0.9;
  }
  .band-rule.top { top: 16px; }
  .band-rule.bottom { bottom: 16px; }
  .brand-name {
    position: absolute;
    left: 0;
    width: 100%;
    top: 80px;
    margin: 0;
    text-align: center;
    color: var(--white);
    font-size: 62px;
    font-weight: 700;
    letter-spacing: 1px;
  }
  .brand-tagline {
    position: absolute;
    left: 0;
    width: 100%;
    top: 158px;
    margin: 0;
    text-align: center;
    color: var(--white);
    font-family: "Delius", "Comic Sans MS", cursive;
    font-size: 34px;
  }
  .contact-list {
    position: absolute;
    left: 38px;
    top: 414px;
    margin: 0;
    padding: 0;
    list-style: none;
  }
  .contact-item {
    display: flex;
    align-items: center;
    gap: 16px;
    height: 46px;
    font-size: 25px;
    font-weight: 700;
    color: var(--ink);
  }
  .contact-icon { flex: none; }
</style>
</head>
<body>
  <div class="business-card">
    <div class="owner-block">
      <p class="owner-name">Marisol Penwarden</p>
      <p class="owner-title">Owner</p>
    </div>

    <div class="phone">
      <svg class="contact-icon" width="38" height="38" viewBox="0 0 38 38" aria-hidden="true">
        <circle cx="19" cy="19" r="19" fill="var(--brand-orange)"/>
        <path d="M9 16 q10 -8 20 0 l-2 3 -4 -1 0 -2 q-4 -2 -8 0 l0 2 -4 1z" fill="#fff"/>
        <rect x="12" y="19" width="14" height="9" rx="2" fill="#fff"/>
        <circle cx="19" cy="23.5" r="2.2" fill="var(--brand-orange)"/>
      </svg>
      <span>617-555-0193</span>
    </div>

    <div class="brand-band">
      <div class="band-rule top"></div>
      <h1 class="brand-name">Harborlux</h1>
      <p class="brand-tagline">Guiding Every Step Together</p>
      <div class="band-rule bottom"></div>
    </div>

    <ul class="contact-list">
      <li class="contact-item">
        <svg class="contact-icon" width="30" height="30" viewBox="0 0 30 30" aria-hidden="true">
          <circle cx="15" cy="15" r="15" fill="var(--brand-orange)"/>
          <rect x="7" y="9.5" width="16" height="11" rx="1.5" fill="#fff"/>
          <path d="M7.5 10.5 L15 16 L22.5 10.5" fill="none" stroke="var(--brand-orange)" stroke-width="1.6"/>
        </svg>
        <span>mpenwarden@harborluxparenting.com</span>
      </li>
      <li class="contact-item">
        <svg class="contact-icon" width="30" height="30" viewBox="0 0 30 30" aria-hidden="true">
          <circle cx="15" cy="15" r="15" fill="var(--brand-orange)"/>
          <g fill="none" stroke="#fff" stroke-width="1.5">
            <circle cx="15" cy="15" r="8"/>
            <ellipse cx="15" cy="15" rx="3.5" ry="8"/>
            <line x1="7" y1="15" x2="23" y2="15"/>
            <line x1="8.5" y1="11" x2="21.5" y2="11"/>
            <line x1="8.5" y1="19" x2="21.5" y2="19"/>
          </g>
        </svg>
        <span>www.harborluxparenting.com</span>
      </li>
      <li class="contact-item">
        <svg class="contact-icon" width="30" height="30" viewBox="0 0 30 30" aria-hidden="true">
          <circle cx="15" cy="15" r="15" fill="var(--brand-orange)"/>
        </svg>
        <span>Kinbook.com/HarborluxParenting</span>
      </li>
    </ul>
  </div>
</body>
</html>
```